M&A Advisory firm needs elegant and powerful letterhead

We need a powerful but elegant letterhead to engage with the international financial industry.

Target Market(s)

New York and International Financial Industry

Industry/Entity Type

Finance

Font styles to use
Other font styles liked:
• Poppins

Requirements
Must have
• 482 W 71st Street 14th Floor New York, NY 10157 O: +1 (212) 555 0147 F: +1 (212) 555 0182

```html
<!DOCTYPE html>
<html lang="en">
<head>
<meta charset="UTF-8">
<title>Norvane Letterhead</title>
<link href="https://fonts.googleapis.com/css2?family=Poppins:wght@400&display=swap" rel="stylesheet">
<style>
  :root {
    --brand-blue: #0f5596;
    --tag-grey: #6f6f6f;
    --rule-dark: #1a1a1a;
    --paper: #ffffff;
  }
  html, body {
    margin: 0;
    padding: 0;
    overflow: hidden;
    background: var(--paper);
  }
  .letterhead {
    position: relative;
    width: 848px;
    height: 1200px;
    background: var(--paper);
    font-family: "Poppins", sans-serif;
    overflow: hidden;
  }
  .brand {
    position: absolute;
    top: 76px;
    left: 0;
    width: 848px;
    display: flex;
    justify-content: center;
    align-items: center;
    gap: 14px;
  }
  .brand-dot {
    width: 22px;
    height: 22px;
    border-radius: 50%;
    background: var(--brand-blue);
  }
  .brand-text {
    display: flex;
    flex-direction: column;
  }
  .brand-name {
    font-size: 42px;
    line-height: 1;
    color: var(--brand-blue);
    letter-spacing: 1px;
  }
  .brand-tagline {
    margin-top: 6px;
    font-size: 9.5px;
    letter-spacing: 3px;
    color: var(--brand-blue);
  }
  .rule {
    position: absolute;
    display: block;
  }
  .rule-header { left: 140px; top: 139px; }
  .rule-footer-top { left: 44px; top: 1113px; }
  .rule-footer-bottom { left: 44px; top: 1159px; }
  .contact-bar {
    position: absolute;
    left: 44px;
    top: 1125px;
    width: 764px;
    height: 30px;
    display: flex;
    align-items: center;
    justify-content: space-between;
    font-size: 16.4px;
    color: var(--brand-blue);
    white-space: nowrap;
  }
  .contact-divider {
    width: 1.5px;
    height: 25px;
    background: var(--rule-dark);
  }
</style>
</head>
<body>
  <div class="letterhead">
    <header class="brand">
      <span class="brand-dot"></span>
      <div class="brand-text">
        <span class="brand-name">NORVANE</span>
        <span class="brand-tagline">Bridging the Deals</span>
      </div>
    </header>

    <svg class="rule rule-header" width="596" height="6" viewBox="0 0 596 6" aria-hidden="true">
      <path d="M0 3 Q298 0 596 3 Q298 6 0 3 Z" fill="var(--brand-blue)"/>
    </svg>

    <svg class="rule rule-footer-top" width="764" height="5" viewBox="0 0 764 5" aria-hidden="true">
      <path d="M0 2.5 Q382 -0.5 764 2.5 Q382 5.5 0 2.5 Z" fill="var(--brand-blue)"/>
    </svg>

    <footer class="contact-bar">
      <span class="contact-address">482 W 71st Street 14th Floor New York, NY 10157</span>
      <span class="contact-divider"></span>
      <span class="contact-office">O: +1 (212) 555 0147</span>
      <span class="contact-divider"></span>
      <span class="contact-fax">F: +1 (212) 555 0182</span>
    </footer>

    <svg class="rule rule-footer-bottom" width="764" height="5" viewBox="0 0 764 5" aria-hidden="true">
      <path d="M0 2.5 Q382 -0.5 764 2.5 Q382 5.5 0 2.5 Z" fill="var(--brand-blue)"/>
    </svg>
  </div>
</body>
</html>
```